Bref créative
Stationery design for KORV Holdings
KORV Holdings - Motion Lessons & Media
Use same font as used in my logo
Trajan Bold
Bright & Fun-filled
Damian Whitcombe
IT & Technical Support
The Lumley House
12 Fenwick Lane
Ashcombe-Under-Lyne
Bristol
BS4 7QD
damian@korv.co
www.korv.co
This is the KORV Holdings logo.

```html
<!DOCTYPE html>
<html lang="en">
<head>
<meta charset="UTF-8">
<title>KORV Holdings — Business Card</title>
<link href="https://fonts.googleapis.com/css2?family=Cinzel:wght@400;700&family=Cormorant+Garamond:ital,wght@0,500;1,500&display=swap" rel="stylesheet">
<style>
  :root{
    --gold:#c9a21a;
    --gold-deep:#b08a0c;
    --gold-light:#e2be3a;
    --paper:#ffffff;
    --paper-shade:#f1f1ef;
    --backdrop:#e9e9e7;
    --ink-soft:#8a7a3a;
  }
  *{margin:0;padding:0;box-sizing:border-box}
  html,body{width:1200px;height:980px;overflow:hidden}
  body{
    background:var(--backdrop);
    display:flex;flex-direction:column;align-items:center;justify-content:center;gap:44px;
    font-family:"Cormorant Garamond", serif;
  }
  .card{
    position:relative;width:760px;height:434px;border-radius:26px;overflow:hidden;
    box-shadow:0 6px 18px rgba(0,0,0,.12);
  }
  /* Back */
  .card-back{
    background:radial-gradient(ellipse at 45% 40%, var(--gold-light) 0%, var(--gold) 55%, var(--gold-deep) 100%);
    display:flex;flex-direction:column;align-items:center;justify-content:center;color:var(--paper);
  }
  .card-back .brand-name{
    font-family:"Cinzel", serif;font-weight:700;font-size:92px;letter-spacing:4px;line-height:1;
    padding-bottom:10px;border-bottom:2px solid var(--paper);
  }
  .card-back .web{
    font-family:"Cinzel", serif;font-weight:400;font-size:17px;letter-spacing:9px;margin-top:12px;
  }
  /* Front */
  .card-front{
    background:linear-gradient(160deg, var(--paper) 0%, var(--paper) 60%, var(--paper-shade) 100%);
  }
  .accent-area{
    position:absolute;right:-40px;bottom:-40px;width:360px;height:340px;
    border-top-left-radius:100% 100%;
    background:linear-gradient(150deg, var(--gold-light) 0%, var(--gold) 50%, var(--gold-deep) 100%);
  }
  .brand{
    position:absolute;left:44px;top:40px;color:var(--gold);font-family:"Cinzel", serif;font-weight:700;
  }
  .brand .brand-name{font-size:78px;line-height:1;letter-spacing:3px;padding-bottom:6px;border-bottom:3px solid var(--gold)}
  .brand .brand-sub{font-size:17px;letter-spacing:9px;margin-top:8px;text-align:right}
  .contact{
    position:absolute;left:44px;top:190px;list-style:none;color:var(--ink-soft);
    font-size:15px;line-height:20px;
  }
  .contact li{display:flex;align-items:center;gap:9px}
  .contact .dot{width:11px;height:11px;border-radius:50%;background:var(--gold);flex:none}
  .person{
    position:absolute;right:330px;top:262px;text-align:right;color:var(--gold-deep);font-style:italic;
  }
  .person .name{font-family:"Cinzel", serif;font-style:normal;font-size:17px;letter-spacing:1px}
  .person .role{font-size:16px;letter-spacing:1px}
</style>
</head>
<body>
  <section class="card card-back">
    <div class="brand-name">KORV</div>
    <div class="web">WWW.KORV.CO</div>
  </section>

  <section class="card card-front">
    <div class="accent-area" role="img" aria-label="Gold curved accent sweeping up the lower right corner"></div>

    <div class="brand">
      <div class="brand-name">KORV</div>
      <div class="brand-sub">HOLDINGS</div>
    </div>

    <ul class="contact">
      <li><span class="dot"></span>The Lumley House</li>
      <li><span class="dot"></span>12 Fenwick Lane</li>
      <li><span class="dot"></span>Ashcombe-Under-Lyne</li>
      <li><span class="dot"></span>Bristol, BS4 7QD</li>
      <li><span class="dot"></span>T 0117 496 0321</li>
      <li><span class="dot"></span>M 07700 900 412</li>
      <li><span class="dot"></span>damian@korv.co</li>
      <li><span class="dot"></span>www.korv.co</li>
    </ul>

    <div class="person">
      <div class="name">Damian Whitcombe</div>
      <div class="role">IT &amp; Technical Support</div>
    </div>
  </section>
</body>
</html>
```